Business cards with huge impact
Startup accelerator
Project: Business cards with huge impact
Business cards with huge impact - Telecommunications
Creative Brief
Professional
Marta Lezcano Ibarrola
Manager
Edificio Almendro Cl. de Valdebruna 714B. 9th floor. 28093 Madrid, Spain
marta.lezcano@brotevivohub.com
Brotevivohub.com
We are looking for a card that shows a company really modern, technological, INTERNET RELATED, INNOVATIVE, and proffesional. IDEALLY in two colours: our corporate Blue of the logo and white We want to include the sentence "Startups accelerator of academic excellence"
We are open to suggestions. We want to really promote our website in the card.

```html
<!DOCTYPE html>
<html lang="en">
<head>
<meta charset="utf-8">
<title>Brote Vivo Hub — Stationery Set</title>
<link href="https://fonts.googleapis.com/css2?family=Open+Sans:wght@400;600&display=swap" rel="stylesheet">
<style>
:root{
  --bg:#eef0f2;
  --paper:#ffffff;
  --brand:#2f5f8f;
  --brand-deep:#17324f;
  --brand-light:#8fb0cf;
  --ink:#4a5560;
  --muted:#8a949c;
  --dark:#2a2f35;
  --shadow:0 2px 6px rgba(0,0,0,.18);
}
*{margin:0;padding:0;box-sizing:border-box}
html,body{width:1200px;height:422px;overflow:hidden}
body{background:var(--bg);font-family:"Open Sans",sans-serif;color:var(--ink);position:relative}
.piece{position:absolute;background:var(--paper);box-shadow:var(--shadow);overflow:hidden}
.caption{position:absolute;font-size:6px;color:var(--muted);text-align:center}

.brand{display:flex;align-items:center;gap:4px;font-weight:600;color:var(--brand);line-height:1}
.brand-mark{background:var(--brand);display:inline-block}
.brand.on-dark{color:#fff}
.brand.on-dark .brand-mark{background:#fff}

/* business cards */
.card{left:19px;width:144px;height:91px}
.card-front{top:72px;padding:10px 9px}
.card-front .brand{font-size:11px}
.card-front .brand-mark{width:10px;height:10px}
.card-front .person{margin-top:12px;font-size:6px;font-weight:600;color:var(--brand-deep)}
.card-front .details{font-size:4.5px;line-height:1.45;margin-top:2px}
.card-back{top:180px;background:linear-gradient(180deg,var(--brand-light) 0%,var(--brand) 45%,var(--brand-deep) 100%);display:flex;flex-direction:column;align-items:center;justify-content:center;gap:8px}
.card-back .brand{font-size:12px}
.card-back .brand-mark{width:11px;height:11px}
.card-back .web{font-size:5px;color:#dbe7f2}
.card-alt{top:300px;display:flex;flex-direction:column;align-items:center;justify-content:center;gap:7px}
.card-alt .brand{font-size:12px}
.card-alt .brand-mark{width:11px;height:11px}
.card-alt .tagline{font-size:4.8px;color:var(--brand)}

/* letterheads */
.letter{top:24px;width:288px;height:372px}
.letter .brand{position:absolute;left:18px;top:16px;font-size:16px}
.letter .brand-mark{width:15px;height:15px}
.letter .contact{position:absolute;right:18px;top:18px;font-size:4.5px;line-height:1.5;text-align:left;color:var(--muted)}
.letter .decor{position:absolute;left:40px;bottom:38px;width:190px;height:130px;background:radial-gradient(ellipse at 50% 60%,rgba(143,176,207,.32),rgba(143,176,207,0) 70%)}
.letter .band{position:absolute;left:0;right:0;bottom:14px;height:12px;background:linear-gradient(90deg,var(--brand-light),var(--brand-deep) 50%,var(--brand-light))}
.letter .footer{position:absolute;left:0;right:0;bottom:3px;font-size:4px;text-align:center;color:var(--muted)}

/* envelopes */
.env{left:809px;width:379px;height:96px}
.env .brand{font-size:10px}
.env .brand-mark{width:9px;height:9px}
.env-dark{top:24px;background:linear-gradient(180deg,#44494f,var(--dark));display:flex;justify-content:center;padding-top:12px}
.env-blue{top:108px;background:linear-gradient(180deg,var(--brand-deep),var(--brand) 30%,#fff 31%);padding:36px 0 0 120px}
.env-white{top:192px;padding:14px 0 0 18px}
.env-white .line{position:absolute;left:0;right:0;bottom:0;height:5px;background:var(--brand)}
.env-front{top:264px;height:120px;padding:16px 0 0 18px}
.env .addr{font-size:4.2px;line-height:1.5;color:var(--muted);margin-top:4px}
.env-front .flap{position:absolute;left:0;top:0;width:100%;height:100%}
</style>
</head>
<body>

<div class="piece card card-front">
  <div class="brand"><span class="brand-mark"></span>Brote Vivo Hub</div>
  <div class="person">Marta Lezcano Ibarrola</div>
  <div class="details">Manager<br>Edificio Almendro<br>Cl. de Valdebruna 714B. 9th floor. 28093 Madrid, Spain<br>marta.lezcano@brotevivohub.com<br>+34 910 555 214</div>
</div>
<div class="caption" style="left:19px;top:165px;width:144px">Business card front</div>

<div class="piece card card-back">
  <div class="brand on-dark"><span class="brand-mark"></span>Brote Vivo Hub</div>
  <div class="web">Brotevivohub.com</div>
</div>
<div class="caption" style="left:19px;top:285px;width:144px">Business card back</div>

<div class="piece card card-alt">
  <div class="brand"><span class="brand-mark"></span>Brote Vivo Hub</div>
  <div class="tagline">Startups accelerator of academic excellence</div>
</div>
<div class="caption" style="left:19px;top:400px;width:144px">Back card</div>

<div class="piece letter" style="left:204px">
  <div class="brand"><span class="brand-mark"></span>Brote Vivo Hub</div>
  <div class="contact">+34 910 555 214<br>marta.lezcano@brotevivohub.com<br>Brotevivohub.com</div>
  <div class="decor" role="img" aria-label="Faint gears and leaves decoration"></div>
  <div class="band"></div>
  <div class="footer">Edificio Almendro · Cl. de Valdebruna 714B. 9th floor. 28093 Madrid</div>
</div>
<div class="caption" style="left:204px;top:401px;width:288px">Letterhead page one</div>

<div class="piece letter" style="left:509px">
  <div class="decor" role="img" aria-label="Faint gears and leaves decoration"></div>
  <div class="band"></div>
  <div class="footer">Brotevivohub.com</div>
</div>
<div class="caption" style="left:509px;top:401px;width:288px">Letterhead page two</div>

<div class="piece env env-dark">
  <div class="brand on-dark"><span class="brand-mark"></span>Brote Vivo Hub</div>
</div>
<div class="piece env env-blue">
  <div class="brand"><span class="brand-mark"></span>Brote Vivo Hub</div>
</div>
<div class="piece env env-white">
  <div class="brand"><span class="brand-mark"></span>Brote Vivo Hub</div>
  <div class="addr">Edificio Almendro<br>Cl. de Valdebruna 714B. 9th floor. 28093</div>
  <div class="line"></div>
</div>
<div class="piece env env-front">
  <svg class="flap" viewBox="0 0 379 120" preserveAspectRatio="none" aria-hidden="true">
    <polyline points="0,0 189,70 379,0" fill="none" stroke="#d5dbe1" stroke-width="1"/>
  </svg>
  <div class="brand"><span class="brand-mark"></span>Brote Vivo Hub</div>
  <div class="addr">Brotevivohub.com</div>
</div>
<div class="caption" style="left:809px;top:401px;width:379px">Envelope DL set</div>

</body>
</html>
```